LANTERN QUAY PRODUCTION SERVICES needs a Brochure Design

We are a new company based in dubai that specializes in creative media production. We create conceptual tv commercials, corporate videos, music videos, documentaries, short films, training videos, time-lapses, we also cover live events and do photography.
We would like the designer to be creative in their design and also provide text to go with.
Link to our logo: http://www.artbidhub.com/design/482106/logo-design-by-velmora-estudios
We want six pages:
1- Logo with web link at bottom of page
2- About Us
3- Services Offered
4- Equipment List
5- Equipment List continued
6- Contact Us
PS: Use meadowlark & bristlecones Font.
Our Address:
Blgd. Al Sanabel, Off. 342, Al Rimah
Dubai, UAE
T: +9714 512 7068
PoBox. 38205
Web: www.lanternquayhub.com
Please do not copy or create exactly the same "About Us" that is found in the attached files. We are looking for something more professional along the same lines.

```html
<!DOCTYPE html>
<html lang="en">
<head>
<meta charset="utf-8">
<title>Lantern Quay Production Services – Brochure Cover</title>
<link href="https://fonts.googleapis.com/css2?family=Jost:wght@300;400&display=swap" rel="stylesheet">
<style>
  :root {
    --backdrop: #2f2b29;
    --page-light: #968880;
    --page-mid: #7a6c66;
    --page-dark: #4a413e;
    --ink-white: #ffffff;
    --ink-soft: #d9d2ce;
    --accent-red: #d81f26;
    --accent-deep: #6e0f12;
    --accent-orange: #e9962a;
    --accent-yellow: #e6d21c;
  }
  html, body {
    margin: 0;
    padding: 0;
    width: 1200px;
    height: 854px;
    overflow: hidden;
    background: var(--backdrop);
    font-family: "Jost", sans-serif;
  }
  .spread {
    position: absolute;
    left: 66px;
    top: 47px;
    width: 1068px;
    height: 760px;
    display: flex;
    box-shadow: 0 2px 6px rgba(0,0,0,0.45);
  }
  .page {
    position: relative;
    width: 534px;
    height: 760px;
    overflow: hidden;
  }
  .page--back {
    background: radial-gradient(ellipse 95% 85% at 80% 100%, var(--page-light) 0%, var(--page-mid) 45%, var(--page-dark) 100%);
  }
  .page--front {
    background: radial-gradient(ellipse 90% 85% at 35% 90%, var(--page-light) 0%, var(--page-mid) 45%, var(--page-dark) 100%);
    border-left: 1px solid rgba(0,0,0,0.35);
  }
  .brand-mark {
    position: absolute;
    left: 255px;
    top: 432px;
    width: 24px;
    height: 24px;
    background: var(--accent-red);
  }
  .brand {
    position: absolute;
    color: var(--ink-white);
    text-transform: uppercase;
  }
  .brand--back {
    left: 0;
    width: 534px;
    top: 526px;
    text-align: center;
  }
  .brand--front {
    right: 34px;
    top: 330px;
    text-align: right;
  }
  .brand__name {
    font-weight: 300;
    font-size: 25px;
    letter-spacing: 3.2px;
    line-height: 1;
    margin: 0;
  }
  .brand__tagline {
    font-weight: 300;
    font-size: 9.5px;
    letter-spacing: 5px;
    color: var(--ink-soft);
    margin: 4px 0 0;
    line-height: 1;
  }
  .brand__web {
    font-weight: 400;
    font-size: 8.5px;
    letter-spacing: 1.2px;
    text-transform: none;
    color: var(--ink-soft);
    margin: 7px 0 0;
    line-height: 1;
  }
  .address {
    position: absolute;
    left: 0;
    width: 534px;
    top: 610px;
    text-align: center;
    color: var(--ink-white);
    font-size: 12px;
    font-weight: 400;
    line-height: 15.2px;
    font-style: normal;
  }
  .hero-art {
    position: absolute;
    left: 0;
    top: 0;
  }
</style>
</head>
<body>
  <main class="spread">
    <section class="page page--back">
      <span class="brand-mark" aria-hidden="true"></span>
      <header class="brand brand--back">
        <h2 class="brand__name">Lantern Quay</h2>
        <p class="brand__tagline">Production Services</p>
        <p class="brand__web">www.lanternquayhub.com</p>
      </header>
      <address class="address">
        Blgd. Al Sanabel, Off. 342, Al Rimah<br>
        Dubai, UAE<br>
        T: +9714 512 7068<br>
        PoBox. 38205
      </address>
    </section>

    <section class="page page--front">
      <svg class="hero-art" width="240" height="760" viewBox="0 0 240 760" role="img" aria-label="Large red and orange folded-paper bird illustration built from film strip">
        <defs>
          <linearGradient id="heroFill" x1="0" y1="0" x2="0" y2="1">
            <stop offset="0" stop-color="var(--accent-red)"/>
            <stop offset="0.6" stop-color="var(--accent-deep)"/>
            <stop offset="1" stop-color="var(--accent-orange)"/>
          </linearGradient>
        </defs>
        <rect x="0" y="0" width="240" height="760" fill="url(#heroFill)"/>
      </svg>
      <header class="brand brand--front">
        <h1 class="brand__name">Lantern Quay</h1>
        <p class="brand__tagline">Production Services</p>
        <p class="brand__web">www.lanternquayhub.com</p>
      </header>
    </section>
  </main>
</body>
</html>
```